Home Health Agency Marketing Portfolio Booklet

We need a 4 page plus cover (total of 8 pages including front and back cover) design of a Home health Agency Marketing Booklet.
We specialize in taking care of homebound senior patients who needs specialize nursing and medical services in the comfort of their homes. We would like to see a design showing the caring and compassionate nature of our agency. The design should show a nice clean modern layout with nice font selection. Attached is a copy of our logo that needs to be use in the brochure. The colors of the logo should be use in the design of the brochure.
The design will consist of the Front and back cover, inside pages of the cover will be blank but there will be folded pockets that will need some design/color. The inside 4 pages will be full cover, double sided and will have all the information of the company.
The Marketing booklet will be 9"x 12".

```html
<!DOCTYPE html>
<html lang="en">
<head>
<meta charset="utf-8">
<title>Radiant Health Home Care – Booklet Spreads</title>
<link href="https://fonts.googleapis.com/css2?family=Open+Sans:wght@400;600;700&family=Courgette&display=swap" rel="stylesheet">
<style>
:root{
  --blue:#1d8fd0;
  --blue-deep:#157bb8;
  --orange:#f39a1e;
  --orange-light:#f7b234;
  --ink:#555a60;
  --bg:#d9dadc;
  --white:#ffffff;
}
*{margin:0;padding:0;box-sizing:border-box}
html,body{width:994px;height:1200px;overflow:hidden;background:var(--bg)}
body{position:relative;font-family:"Open Sans",Arial,sans-serif;color:var(--ink)}
.spread{position:absolute;left:91px;width:791px;height:528px;display:flex;background:var(--white)}
.spread--one{top:55px}
.spread--two{top:625px}
.page{position:relative;width:395.5px;height:528px;overflow:hidden;background:var(--white)}
.page--right{background:linear-gradient(90deg,#fff 0%,#fff 85%,#ececec 100%)}
.photo{position:absolute;left:0;top:0;width:100%}
.wave{position:absolute;left:0;width:100%}
.band{position:absolute;left:0;bottom:0;width:100%;height:12px;background:linear-gradient(90deg,var(--orange),var(--orange-light),var(--orange))}
.brand{position:absolute;display:flex;align-items:center;gap:6px;font-weight:700;color:var(--blue);font-size:15px;line-height:1.05;letter-spacing:.3px}
.brand-dot{width:26px;height:26px;border-radius:50%;background:var(--orange);flex:none}
.col{position:absolute;font-size:6.3px;line-height:9.2px;text-align:justify}
.col p{margin-bottom:7px}
h2{font-size:8.6px;line-height:12px;font-weight:600;color:var(--blue);text-transform:uppercase}
.rule{display:block;width:72px;height:1.5px;background:var(--orange);margin:3px 0 8px}
.col--blue{color:#fff}
.col--blue h2{color:#fff}
.mission-panel{position:absolute;left:217px;top:200px;width:167px;height:316px;background:linear-gradient(180deg,var(--blue),var(--blue-deep))}
.team-title{position:absolute;left:0;width:100%;top:262px;text-align:center;font-size:11.5px;font-weight:600;color:var(--blue);letter-spacing:.2px}
.team-title::before,.team-title::after{content:"";display:inline-block;width:32px;height:1.5px;background:var(--orange);vertical-align:middle;margin:0 6px}
.bullets li{list-style:none;margin-bottom:7px}
.bullets li::before{content:"• ";color:var(--orange)}
.divider{position:absolute;left:198px;top:290px;width:1px;height:200px;background:#e5e5e5}
.benefits li{list-style:none;display:flex;gap:5px;margin-bottom:6px;text-align:left}
.benefits svg{flex:none;margin-top:1px}
.circle{position:absolute;border-radius:50%;border:3px solid #fff;box-shadow:0 0 0 1.5px var(--orange-light)}
.service h3{font-size:6.4px;font-weight:700;color:var(--blue);text-transform:uppercase;display:flex;align-items:center;gap:3px;margin-top:8px}
.service p{margin-bottom:4px}
.service ul{margin-bottom:2px}
.service li{list-style:none}
.service li::before{content:"• "}
.quote{position:absolute;left:22px;top:34px;width:120px;text-align:center;font-family:"Courgette",cursive;font-size:12.5px;line-height:23px;color:var(--blue)}
</style>
</head>
<body>

<!-- Spread 1 -->
<section class="spread spread--one">
  <article class="page page--left">
    <div class="photo" style="height:210px;background:linear-gradient(135deg,#c9c3ba,#8f9aa6 45%,#2f6fb8 75%,#dcd6cc)" role="img" aria-label="Photo: nurse in blue scrubs helping an elderly man walk at home"></div>
    <div class="mission-panel"></div>
    <svg class="wave" style="top:170px" width="395.5" height="50" viewBox="0 0 395.5 50" aria-hidden="true">
      <path d="M0 12 Q200 60 395.5 10 L395.5 50 L0 50Z" fill="#fff"/>
      <path d="M0 10 Q200 58 395.5 8" fill="none" stroke="var(--orange)" stroke-width="4"/>
    </svg>
    <div class="brand" style="left:19px;top:240px"><span class="brand-dot"></span><span>RADIANT HEALTH<br>HOME CARE</span></div>
    <div class="col" style="left:19px;top:295px;width:188px">
      <h2>Home health care is being given<br>in the comfort of your home</h2>
      <p style="margin-top:4px">You or your loved ones can receive the level of medical care you’d expect from a hospital or doctor’s office, without sacrificing comfort or dealing with the process of leaving home.</p>
      <h2 style="margin-top:12px">About us</h2><span class="rule"></span>
      <p>Radiant Health Home Care is an experienced home health agency that takes pride and confidence in our ability to deliver amazing services for each of our patients. We have established the foundation that health care is better when patients get amazing personalized care at home - the place they would rather be.</p>
      <p>Our agency consists of competent staff that has gained the knowledge, compassion, character, and quality of a home health care service that our patient deserves.</p>
    </div>
    <div class="col col--blue" style="left:230px;top:245px;width:144px">
      <h2>Mission</h2><span class="rule"></span>
      <p>Radiant Health Home Care mission is to provide each patient with an amazing high quality home health care service that will enable them to live comfortably each day and help them manage their illness or health condition in the comfort of their home.</p>
      <h2 style="margin-top:10px">Our Services</h2><span class="rule"></span>
      <p>Radiant Health Home Care is committed to the highest quality in-home patient care services. We have a wide range of skilled care services that we provide in the comfort of your home. We also offer add-on care, and teach the patient and caregivers what they need to know about how to manage care at home.</p>
      <p>Patients that are transitioning from Hospital to home can benefit from this program. Radiant Health Home Care helps the patient get better, regain their independence, become self-sufficient as possible on their way to have an amazing healthier life.</p>
    </div>
    <div class="band"></div>
  </article>

  <article class="page page--right">
    <div class="photo" style="height:205px;background:linear-gradient(135deg,#e9e1d2,#c9b89a 35%,#3b78b8 60%,#5b6470 85%,#d8d2c6)" role="img" aria-label="Photo: nurse chatting with a smiling senior woman seated on a sofa"></div>
    <svg class="wave" style="top:175px" width="395.5" height="50" viewBox="0 0 395.5 50" aria-hidden="true">
      <path d="M0 12 Q200 50 395.5 0 L395.5 50 L0 50Z" fill="#fff"/>
      <path d="M0 10 Q200 48 395.5 -2" fill="none" stroke="var(--orange)" stroke-width="4"/>
    </svg>
    <div class="circle" style="left:87px;top:167px;width:80px;height:80px;background:linear-gradient(135deg,#efe9e2,#b7a89a)" role="img" aria-label="Photo: caregiver with an elderly woman"></div>
    <div class="circle" style="left:157px;top:167px;width:80px;height:80px;background:linear-gradient(135deg,#f0d3bd,#c8927a)" role="img" aria-label="Photo: hands holding in comfort"></div>
    <div class="circle" style="left:227px;top:167px;width:80px;height:80px;background:linear-gradient(135deg,#e9e2d9,#6a5c52)" role="img" aria-label="Photo: hands exercising with small dumbbells"></div>
    <div class="team-title">HOME HEALTH TEAM</div>
    <div class="col" style="left:18px;top:290px;width:169px">
      <p>Home Health Nurse (RNs and LVNs) – Skilled nursing provides patients who suffer from an existing disease or complex health condition with continuous care. They coordinate a patient's plan of care between doctors, hospitals and other home health care team members. The Home Health Nurse portfolio includes, but not limited, to:</p>
      <ul class="bullets">
        <li>Case manage the patient’s medical needs, create a specific plan of care, in consultation with the patient's doctor, with the goal of a rapid recovery.</li>
        <li>Oversees the patient’s health, symptoms and vital signs.</li>
        <li>Educate patients and caregivers about illness and treatment.</li>
        <li>Assist with pain and medication management.</li>
        <li>Monitor and address early symptoms that could lead to hospitalization.</li>
      </ul>
    </div>
    <div class="divider"></div>
    <div class="col" style="left:210px;top:290px;width:172px">
      <ul class="bullets">
        <li>Provides wound care, ostomy care, pre-op and post-op care, treatments and injections, Intravenous Therapy (IV), and other medical services.</li>
        <li>Monitor and address early symptoms that could lead to hospitalization.</li>
      </ul>
      <h2 style="margin:14px 0 6px">Benefits</h2>
      <ul class="benefits">
        <li><svg width="6" height="6" viewBox="0 0 6 6"><circle cx="3" cy="3" r="2.6" fill="var(--blue)"/></svg>Remain in the comfort of your home</li>
        <li><svg width="6" height="6" viewBox="0 0 6 6"><circle cx="3" cy="3" r="2.6" fill="var(--blue)"/></svg>Individualized care designed to meet your specific needs</li>
        <li><svg width="6" height="6" viewBox="0 0 6 6"><circle cx="3" cy="3" r="2.6" fill="var(--blue)"/></svg>Reduced risk of returning to the hospital after a hospital discharge</li>
        <li><svg width="6" height="6" viewBox="0 0 6 6"><circle cx="3" cy="3" r="2.6" fill="var(--blue)"/></svg>Your family can participate in your care</li>
        <li><svg width="6" height="6" viewBox="0 0 6 6"><circle cx="3" cy="3" r="2.6" fill="var(--blue)"/></svg>Maintain your independence and stay at home</li>
      </ul>
    </div>
    <div class="band"></div>
  </article>
</section>

<!-- Spread 2 -->
<section class="spread spread--two">
  <article class="page page--left">
    <div class="photo" style="height:240px;background:linear-gradient(135deg,#3d5a3a,#8aa27a 35%,#ece6dc 55%,#c7b8a6 75%,#2e6fb5)" role="img" aria-label="Photo: caregiver holding the hand of a smiling senior woman outdoors"></div>
    <svg class="wave" style="top:170px" width="395.5" height="80" viewBox="0 0 395.5 80" aria-hidden="true">
      <path d="M0 20 Q180 90 395.5 40 L395.5 80 L0 80Z" fill="#fff"/>
      <path d="M0 28 Q180 88 395.5 40" fill="none" stroke="var(--blue)" stroke-width="4"/>
      <path d="M0 18 Q180 80 395.5 34" fill="none" stroke="var(--orange)" stroke-width="5"/>
    </svg>
    <div class="col service" style="left:19px;top:261px;width:358px">
      <h2 style="font-size:10.5px">Your way to an amazing health</h2><span class="rule"></span>
      <h3><svg width="7" height="7" viewBox="0 0 8 8"><circle cx="4" cy="4" r="3.3" fill="none" stroke="var(--orange)" stroke-width=".9"/><path d="M2.3 4.1l1.2 1.2 2.3-2.5" fill="none" stroke="var(--blue)" stroke-width=".9"/></svg>Physical Therapist</h3>
      <p>Physical therapist helps build strength and balance so that patients can become safer and more self-sufficient at home. They will help patient return to their prior level of function following illness or injury, or, if not possible, helps them adapt to new ways of moving.</p>
      <p>The Physical Therapist services includes, but not limited, to:</p>
      <ul>
        <li>Focus on exercises and activities to improve balance, strength, and endurance to reduce the risk of falls.</li>
        <li>Evaluate the need for and train in the use of devices such as walkers, cane and wheelchair.</li>
        <li>Advises patients and caregivers about in-home treatment options and exercises</li>
      </ul>
      <h3 style="margin-top:14px"><svg width="7" height="7" viewBox="0 0 8 8"><circle cx="4" cy="4" r="3.3" fill="none" stroke="var(--orange)" stroke-width=".9"/><path d="M2.3 4.1l1.2 1.2 2.3-2.5" fill="none" stroke="var(--blue)" stroke-width=".9"/></svg>Occupational Therapist</h3>
      <p>Occupational therapist recognizes that the most ideal place to get better is at home. They will help patients and their caregivers learn personalized adaptations for performing their daily activities more safely and independently in their home.</p>
      <p>The Occupational Therapist services includes, but not limited, to:</p>
      <ul>
        <li>Evaluate and suggest changes in the home environment to improve safety and reduce fall risk.</li>
        <li>Educate patients safely to complete daily tasks like bathing, dressing and everyday household function.</li>
        <li>Instruct patients using special equipment, like shower chair or bedside commodes.</li>
      </ul>
    </div>
    <div class="band"></div>
  </article>

  <article class="page page--right">
    <div class="photo" style="left:140px;width:256px;height:175px;background:linear-gradient(90deg,#fff 0%,#e6ddd2 20%,#c9b3a0 45%,#3b7dc0 75%,#e9e3da)" role="img" aria-label="Photo: nurse smiling with a senior woman at home"></div>
    <div class="quote">The More We Care,<br>The More Amazing<br>Life Becomes</div>
    <svg class="wave" style="top:130px" width="395.5" height="80" viewBox="0 0 395.5 80" aria-hidden="true">
      <path d="M0 70 Q180 20 395.5 30 L395.5 80 L0 80Z" fill="#fff"/>
      <path d="M0 72 Q180 18 395.5 28" fill="none" stroke="var(--orange)" stroke-width="3"/>
      <path d="M330 70 L395.5 60 L395.5 66Z" fill="var(--blue)"/>
    </svg>
    <div class="circle" style="left:207px;top:126px;width:73px;height:73px;background:linear-gradient(135deg,#cfd9e6,#3a78ba 55%,#8a7d70)" role="img" aria-label="Photo: nurse assisting a senior man"></div>
    <div class="circle" style="left:282px;top:135px;width:92px;height:92px;background:linear-gradient(135deg,#b8cfa6,#2f72b8 50%,#d9d2c8)" role="img" aria-label="Photo: caregiver talking with a senior man"></div>
    <div class="brand" style="left:23px;top:200px"><span class="brand-dot"></span><span>RADIANT HEALTH<br>HOME CARE</span></div>
    <div class="col service" style="left:18px;top:248px;width:358px">
      <h3><svg width="7" height="7" viewBox="0 0 8 8"><circle cx="4" cy="4" r="3.3" fill="none" stroke="var(--orange)" stroke-width=".9"/><path d="M2.3 4.1l1.2 1.2 2.3-2.5" fill="none" stroke="var(--blue)" stroke-width=".9"/></svg>Speech Therapist</h3>
      <p>Speech Therapist will assist our patients with conditions such as motor speech disorders, swallowing difficulty, loss of language ability, and cognitive and memory conditions. They are great tools in assessment and interventions for conditions such as Parkinson’s disease, stroke, ALS, dementia, COPD or CHF.</p>
      <p>The Occupational Therapist services includes, but not limited, to:</p>
      <ul>
        <li>Establish verbal or nonverbal system to improve communication Develop programs with structure memory task, problem solving, reasoning, visual and auditory aids, and calendars to assist cognitive impairments</li>
        <li>Helps patient with swallowing difficulties modify their diets, learn safe swallow strategies and practice in-home exercises</li>
      </ul>
      <h3 style="margin-top:10px"><svg width="7" height="7" viewBox="0 0 8 8"><circle cx="4" cy="4" r="3.3" fill="none" stroke="var(--orange)" stroke-width=".9"/><path d="M2.3 4.1l1.2 1.2 2.3-2.5" fill="none" stroke="var(--blue)" stroke-width=".9"/></svg>Medical Social Services</h3>
      <p>Medical social service provides helpful information and assistance to patients and their family members to cope with the short-term and long-term challenges by connecting them with community resources and options available to them. The Medical Social Services includes, but not limited, to:</p>
      <ul>
        <li>Provides counseling and teaches coping skills</li>
        <li>Help patients access financial assistance and health insurance coverage</li>
        <li>Assist with longer term planning following home health services, such as advance care planning, healthcare directives, and financial assistance.</li>
      </ul>
      <h3 style="margin-top:10px"><svg width="7" height="7" viewBox="0 0 8 8"><circle cx="4" cy="4" r="3.3" fill="none" stroke="var(--orange)" stroke-width=".9"/><path d="M2.3 4.1l1.2 1.2 2.3-2.5" fill="none" stroke="var(--blue)" stroke-width=".9"/></svg>Home Health Aides</h3>
      <p>Home health aides will help you with your daily activities such as therapy-driven exercise and personal care and grooming needs. The Home Health Aide services include, but not limited, to:</p>
      <ul>
        <li>Assist in daily task such as bathing, dressing and eating</li>
        <li>Recognizes and communicates changes in patients’ health status to the home health care team.</li>
      </ul>
    </div>
    <div class="band"></div>
  </article>
</section>

</body>
</html>
```